Brivolt VoIP COMMERCIAL PHONE FLYER

We are a full service telecom VoIP company that offers local, long distance calling plans to business clients. We offer local installations, and local service we have a hands on approach and will match or beat any competitor. We work with all types of business. We are fully HIPPA complient in the medical field

Target Market(s)

SMALL TO MEDIUM BUSINESS, Medical, Real Estate, Lawyer, Accounting

Industry/Entity Type

VoIP

Font styles to use
Serif

Colors
0054AA
0677BA
7BADD7
CADEEF
E8F1F8

Requirements
Must have
• Modern/ Current picture of phone reader friendly
Nice to have
• free flow, friendly, modern
Should not have
• stuffy, corporate feel

```html
<!DOCTYPE html>
<html lang="en">
<head>
<meta charset="utf-8">
<title>Brivolt VoIP – Business Phone Flyer</title>
<link href="https://fonts.googleapis.com/css2?family=Oswald:wght@300;400;500&family=Architects+Daughter&display=swap" rel="stylesheet">
<style>
  :root {
    --page-bg: #0b0b0d;
    --navy: #15115c;
    --navy-deep: #120d4f;
    --charcoal: #1f2231;
    --brand-blue: #0677ba;
    --section-blue: #1c6aa5;
    --accent-cyan: #2ea3dc;
    --logo-blue: #1f7fc0;
    --ink-navy: #16124e;
    --white: #ffffff;
    --footer-text: #dfe6f0;
  }
  * { box-sizing: border-box; margin: 0; padding: 0; }
  html, body { width: 1200px; height: 800px; overflow: hidden; background: var(--page-bg); }
  body { position: relative; font-family: "Oswald", "Arial Narrow", sans-serif; }

  .flyer {
    position: absolute; left: 310px; top: 25px;
    width: 580px; height: 750px; overflow: hidden;
  }

  /* hero */
  .hero { position: absolute; left: 0; top: 0; width: 580px; height: 266px; background: var(--navy); }
  .hero__photo {
    position: absolute; left: 18px; top: 16px; width: 286px; height: 236px;
    border-radius: 24px;
    background:
      radial-gradient(ellipse 46% 40% at 62% 42%, rgba(190, 214, 236, 0.55) 0%, rgba(190, 214, 236, 0) 100%),
      radial-gradient(ellipse 70% 62% at 48% 52%, #3a3c45 0%, #25262d 55%, rgba(21, 17, 92, 0) 100%);
  }
  .hero__copy { position: absolute; left: 302px; top: 12px; width: 270px; }
  .hero__kicker { font-weight: 400; font-size: 34px; color: var(--accent-cyan); line-height: 1; margin-left: 20px; }
  .hero__free { font-weight: 500; font-size: 124px; color: var(--white); line-height: 0.96; letter-spacing: -2px; margin-left: 14px; }
  .hero__lines { font-weight: 400; font-size: 34px; color: var(--white); line-height: 1.05; margin-top: 2px; margin-left: 12px; }
  .hero__for { font-weight: 400; font-size: 29px; color: var(--accent-cyan); line-height: 1.15; }

  /* brand band */
  .brand-band { position: absolute; left: 0; top: 266px; width: 580px; height: 80px; background: var(--charcoal); }
  .brand-band__logo { position: absolute; left: 60px; top: 20px; display: flex; align-items: center; gap: 12px; }
  .brand-band__mark { width: 34px; height: 34px; border-radius: 50%; background: var(--logo-blue); }
  .brand-band__name { font-weight: 500; font-size: 38px; color: var(--logo-blue); line-height: 1; }
  .brand-band__tagline { position: absolute; right: 16px; top: 8px; text-align: right; font-family: "Architects Daughter", cursive; color: var(--white); }
  .brand-band__tagline-small { font-size: 26px; line-height: 1; margin-right: 50px; }
  .brand-band__tagline-big { font-size: 41px; line-height: 1.05; }

  /* savings */
  .savings { position: absolute; left: 0; top: 346px; width: 580px; height: 331px; background: var(--section-blue); }
  .savings__lead { position: absolute; left: 35px; top: 16px; font-weight: 400; font-size: 31px; color: var(--ink-navy); line-height: 1.3; }
  .savings__headline { position: absolute; left: 32px; top: 50px; font-weight: 500; font-size: 80px; color: var(--white); line-height: 1.1; letter-spacing: -0.5px; }
  .savings__sub { position: absolute; left: 35px; top: 136px; font-weight: 400; font-size: 28px; color: var(--ink-navy); letter-spacing: -0.6px; line-height: 1.3; }
  .savings__badge {
    position: absolute; left: 393px; top: 19px; width: 157px; height: 157px; border-radius: 50%;
    background: var(--navy-deep); display: flex; align-items: center; justify-content: center;
    font-weight: 500; font-size: 62px; color: var(--white);
  }
  .features { position: absolute; left: 0; top: 202px; width: 580px; display: flex; justify-content: space-between; padding: 0 82px 0 80px; }
  .feature { width: 104px; text-align: center; }
  .feature__icon {
    width: 78px; height: 78px; border-radius: 50%; background: var(--navy-deep); margin: 0 auto 8px;
    display: flex; align-items: center; justify-content: center;
  }
  .feature__label { font-family: "Architects Daughter", cursive; font-size: 15px; line-height: 1.1; color: var(--ink-navy); }

  /* footer */
  .contact-bar {
    position: absolute; left: 0; top: 677px; width: 580px; height: 73px; background: var(--charcoal);
    display: flex; align-items: center; justify-content: center; gap: 18px;
    font-weight: 400; font-size: 16px; color: var(--footer-text); letter-spacing: 1.2px;
  }
  .contact-bar__item { display: flex; align-items: center; gap: 8px; }
  .contact-bar__divider { width: 1px; height: 20px; background: var(--accent-cyan); }
</style>
</head>
<body>
<main class="flyer">
  <section class="hero">
    <div class="hero__photo" role="img" aria-label="Photo of a modern desk video phone with handset and a touchscreen showing a video call"></div>
    <div class="hero__copy">
      <p class="hero__kicker">WE OFFER</p>
      <h1 class="hero__free">FREE</h1>
      <p class="hero__lines">TELEPHONE LINES</p>
      <p class="hero__for">FOR YOUR BUSINESS</p>
    </div>
  </section>

  <section class="brand-band">
    <div class="brand-band__logo">
      <span class="brand-band__mark"></span>
      <span class="brand-band__name">Brivolt</span>
    </div>
    <div class="brand-band__tagline">
      <p class="brand-band__tagline-small">YOUR BUSINESS</p>
      <p class="brand-band__tagline-big">ON THE CLOUD</p>
    </div>
  </section>

  <section class="savings">
    <p class="savings__lead">WE HELP COMPANIES</p>
    <h2 class="savings__headline">SAVE OVER</h2>
    <p class="savings__sub">ON THEIR MONTHLY PHONE BILLS</p>
    <div class="savings__badge">30%</div>

    <div class="features">
      <div class="feature">
        <div class="feature__icon">
          <svg width="44" height="44" viewBox="0 0 44 44" fill="none" stroke="#fff" stroke-width="2" stroke-linecap="round">
            <path d="M22 11a9 9 0 0 0-5 16.5V31h10v-3.5A9 9 0 0 0 22 11z"/>
            <path d="M18 34h8M19 37h6"/>
            <path d="M22 3v4M8 9l3 3M36 9l-3 3M4 21h4M36 21h4"/>
          </svg>
        </div>
        <p class="feature__label">POWERFUL<br>FEATURES</p>
      </div>
      <div class="feature">
        <div class="feature__icon">
          <svg width="46" height="42" viewBox="0 0 46 42">
            <path d="M18 4C9 4 3 9.5 3 16c0 3.5 1.8 6.6 4.7 8.7L6 31l7.2-3.6c1.5.4 3.1.6 4.8.6 9 0 15-5.5 15-12S27 4 18 4z" fill="#fff"/>
            <path d="M30 18c7 0 13 4.5 13 10 0 2.8-1.4 5.2-3.8 7l1.4 5-5.8-2.8c-1.5.5-3.1.8-4.8.8-7 0-13-4.5-13-10" fill="none" stroke="#fff" stroke-width="2.2"/>
            <path d="M13 21v-6h3v6zM17 21v-6l3-5c1.5 0 2 1 1.6 2.5L21 15h4c1 0 1.5.8 1.3 1.7l-1 3.3c-.3.7-.8 1-1.5 1z" fill="#16124e"/>
          </svg>
        </div>
        <p class="feature__label">EASY<br>TO USE</p>
      </div>
      <div class="feature">
        <div class="feature__icon">
          <svg width="44" height="44" viewBox="0 0 44 44" fill="none" stroke="#fff" stroke-width="3" stroke-linecap="round">
            <path d="M10 34l18-18"/>
            <path d="M26 8l10 10-4 4-10-10z" fill="#fff"/>
            <path d="M34 34L16 16"/>
            <path d="M14 8a6 6 0 0 0-6 8l4 2 4-4-2-4z" fill="#fff" stroke-width="1.5"/>
          </svg>
        </div>
        <p class="feature__label">EASY<br>SET UP</p>
      </div>
    </div>
  </section>

  <footer class="contact-bar">
    <span class="contact-bar__item">
      <svg width="16" height="16" viewBox="0 0 24 24" fill="none" stroke="#dfe6f0" stroke-width="2"><path d="M5 3h4l2 5-2.5 1.5a11 11 0 0 0 6 6L16 13l5 2v4a2 2 0 0 1-2 2A16 16 0 0 1 3 5a2 2 0 0 1 2-2z"/></svg>
      1555-010 02468
    </span>
    <span class="contact-bar__divider"></span>
    <span class="contact-bar__item">
      <svg width="20" height="16" viewBox="0 0 24 18" fill="none" stroke="#dfe6f0" stroke-width="2"><path d="M2 6l10-5 10 5v11H2z"/><path d="M2 6l10 6 10-6"/></svg>
      HELLO@BRIVOLT.COM
    </span>
    <span class="contact-bar__divider"></span>
    <span class="contact-bar__item">
      <svg width="16" height="16" viewBox="0 0 24 24" fill="none" stroke="#dfe6f0" stroke-width="2" stroke-linecap="round"><path d="M10 14a5 5 0 0 0 7 0l3-3a5 5 0 0 0-7-7l-1 1"/><path d="M14 10a5 5 0 0 0-7 0l-3 3a5 5 0 0 0 7 7l1-1"/></svg>
      WWW.BRIVOLT.COM
    </span>
  </footer>
</main>
</body>
</html>
```